Design our Hot Cup Jacket / Coffee Sleeve

I am looking for a chic and eye catchy design (using our logo) to put on our coffee cup sleeve to include our Cafe and our coffee truck. We do not need separate design. Both the Cafe and the coffee truck can be represented on the same Coffee Sleeve design. I have provided both logos; one for our Cafe which is called Marigold Cafe & Coffee Bar and the other logo is for our coffee truck which is called The Little Kettle. We would like a back and front design. Can you please include our instragram - marigoldcafeqrx and thelittlekettleqrx

Our Cafe serves breakfast and lunch consisting of full breakfast (pancakes, eggs, bacon, home fries, omeletts etc), lunch (made to order sandwiches and wraps, homemade soups, salads) and freshly baked scones, muffins, pies and cakes. I have also attached a few pictures of the Cafe food, outside on the deck of our Cafe and the Coffee Truck.

Target Market(s)

customers

Industry/Entity Type

Cafe, restaurant, coffee truck

Requirements
Must have
• logo, Instagram name, chic and classy, our logo color
Nice to have
• pictures

```html
<!DOCTYPE html>
<html lang="en">
<head>
<meta charset="utf-8">
<title>Cup Sleeve Design – Marigold Cafe &amp; The Little Kettle</title>
<link rel="stylesheet" href="https://fonts.googleapis.com/css2?family=Oswald:wght@300;600&family=Poppins:wght@800&display=swap">
<style>
  :root {
    --espresso: #4f2629;
    --latte: #dcae93;
    --blush: #e7c3b3;
    --ink: #1c1414;
    --mocha: #5a3030;
  }
  * { margin: 0; padding: 0; box-sizing: border-box; }
  html, body { width: 1200px; height: 1121px; overflow: hidden; background: var(--espresso); }
  .board { position: relative; width: 1200px; height: 1121px; background: var(--espresso); }

  .logo-panel {
    position: absolute; top: 0; height: 379px; background: var(--latte);
    display: flex; flex-direction: column; align-items: center; justify-content: center;
  }
  .logo-panel--truck { left: 63px; width: 487px; }
  .logo-panel--cafe { left: 677px; width: 460px; }

  .brand-name {
    font-family: "Oswald", sans-serif; font-weight: 600; color: var(--ink);
    font-size: 44px; line-height: 1; letter-spacing: 0.5px; text-align: center;
  }
  .brand-name--cafe { font-size: 40px; }
  .handle {
    margin-top: 58px; display: flex; align-items: center; gap: 10px;
    font-family: "Oswald", sans-serif; font-weight: 300; color: var(--mocha); font-size: 30px;
  }
  .handle__mark { width: 24px; height: 24px; border: 3px solid var(--mocha); border-radius: 6px; }

  .section-title {
    position: absolute; left: 0; width: 1200px; text-align: center;
    font-family: "Poppins", sans-serif; font-weight: 800; color: var(--latte);
    font-size: 84px; line-height: 1; letter-spacing: 1px;
  }
  .section-title--design { top: 402px; }

  .stage { position: absolute; left: 0; top: 507px; width: 1200px; height: 450px; background: var(--blush); }

  .sleeve {
    position: absolute; top: 172px; width: 212px; height: 150px;
    display: grid; grid-template-columns: 38px 1fr 38px;
  }
  .sleeve--front { left: 198px; }
  .sleeve--back { left: 797px; }
  .sleeve__edge { background: var(--espresso); }
  .sleeve__face {
    background: var(--latte); display: flex; flex-direction: column;
    align-items: center; justify-content: center; padding: 0 6px;
  }
  .sleeve .brand-name { font-size: 17px; }
  .sleeve .handle { margin-top: 18px; font-size: 10px; gap: 4px; }
  .sleeve .handle__mark { width: 9px; height: 9px; border-width: 1.5px; border-radius: 2px; }

  .side-label {
    position: absolute; top: 992px;
    font-family: "Poppins", sans-serif; font-weight: 800; color: var(--latte);
    font-size: 90px; line-height: 1;
  }
  .side-label--front { left: 158px; }
  .side-label--back { left: 846px; }
</style>
</head>
<body>
<main class="board">
  <section class="logo-panel logo-panel--truck">
    <h2 class="brand-name">The Little Kettle</h2>
    <p class="handle"><span class="handle__mark"></span>thelittlekettleqrx</p>
  </section>
  <section class="logo-panel logo-panel--cafe">
    <h2 class="brand-name brand-name--cafe">Marigold Cafe &amp; Coffee Bar</h2>
    <p class="handle"><span class="handle__mark"></span>marigoldcafeqrx</p>
  </section>

  <h1 class="section-title section-title--design">DESIGN</h1>

  <section class="stage">
    <div class="sleeve sleeve--front">
      <span class="sleeve__edge"></span>
      <div class="sleeve__face">
        <p class="brand-name">The Little Kettle</p>
        <p class="handle"><span class="handle__mark"></span>thelittlekettleqrx</p>
      </div>
      <span class="sleeve__edge"></span>
    </div>
    <div class="sleeve sleeve--back">
      <span class="sleeve__edge"></span>
      <div class="sleeve__face">
        <p class="brand-name">Marigold Cafe</p>
        <p class="handle"><span class="handle__mark"></span>marigoldcafeqrx</p>
      </div>
      <span class="sleeve__edge"></span>
    </div>
  </section>

  <p class="side-label side-label--front">FRONT</p>
  <p class="side-label side-label--back">BACK</p>
</main>
</body>
</html>
```